New Business Card/Website Logo

We need a business card design for a new company based in Sydney. The company focuses mainly in construction in the field of form work and concreting. Attached is the logo being used already which can be used as a base for a new design, the current one is simply too bland and we are looking to spruce it up so it stands out and looks nicer. The logo would also be used on the website which is currently under construction. The attached image has the name, mobile and also the license number which needs to be there. The current email address on there can be removed and can be replaced with the website http://www.bravelintel.com.au, thanks!
Updates

Target Market(s)

Construction industry. Focusing on form work and concreting

Industry/Entity Type

Construction

Requirements
Must have
• License # on card along with website http://www.bravelintel.com.au and mobile phone number
Nice to have
• You have freedom with the design. The current design was a mock up done quite quickly. Please just keep in mind the target audience - construction, thanks.
Should not have
• the mailvista email address can be removed(refer picture) and replaced somewhere on the design with the website http://www.bravelintel.com.au

```html
<!DOCTYPE html>
<html lang="en">
<head>
<meta charset="utf-8">
<title>Bravelintel Business Card</title>
<link rel="stylesheet" href="https://fonts.googleapis.com/css2?family=Questrial&display=swap">
<style>
  :root {
    --backdrop-light: #f1f1f1;
    --backdrop-dark: #cfcfcf;
    --brand-green: #45a03a;
    --brand-green-light: #6cbf55;
    --brand-green-deep: #3a8f31;
    --charcoal: #2b2b2d;
    --white: #ffffff;
    --white-soft: rgba(255, 255, 255, 0.92);
  }
  * { margin: 0; padding: 0; box-sizing: border-box; }
  html, body {
    width: 1200px;
    height: 898px;
    overflow: hidden;
  }
  body {
    background: radial-gradient(ellipse at 50% 35%, var(--backdrop-light) 0%, var(--backdrop-dark) 100%);
    font-family: "Questrial", "Century Gothic", sans-serif;
    position: relative;
  }
  .business-card {
    position: absolute;
    left: 100px;
    top: 171px;
    width: 1000px;
    height: 556px;
    background: var(--charcoal);
    overflow: hidden;
    box-shadow: 0 18px 40px rgba(0, 0, 0, 0.22);
  }
  .card-brand-panel {
    position: absolute;
    left: 0;
    top: 0;
    width: 590px;
    height: 100%;
    background: linear-gradient(135deg, var(--brand-green-light) 0%, var(--brand-green) 45%, var(--brand-green-deep) 100%);
  }
  .contact-band {
    position: absolute;
    left: 560px;
    top: 150px;
    width: 440px;
    height: 112px;
    background: var(--brand-green);
    color: var(--white);
    text-align: right;
    padding: 20px 42px 0 0;
  }
  .contact-name {
    font-size: 32px;
    line-height: 1.15;
  }
  .contact-phone {
    font-size: 28px;
    line-height: 1.2;
  }
  .company-name {
    position: absolute;
    left: 64px;
    top: 232px;
    font-size: 58px;
    color: var(--white);
    letter-spacing: 0.5px;
  }
  .company-details {
    position: absolute;
    left: 64px;
    top: 410px;
    color: var(--white-soft);
    font-size: 27px;
    line-height: 1.35;
  }
</style>
</head>
<body>
  <div class="business-card">
    <div class="card-brand-panel" role="img" aria-label="Faceted green low-poly texture"></div>
    <div class="company-name">bravelintel</div>
    <div class="company-details">
      <p class="licence-number">Licence: 184392B</p>
      <p class="website">www.bravelintel.com.au</p>
    </div>
    <div class="contact-band">
      <p class="contact-name">Marco Ellison</p>
      <p class="contact-phone">0400128473</p>
    </div>
  </div>
</body>
</html>
```